Atelier Greta Voss Coming Soon

Launching a online mid century furniture business. I'm participating in an antiques fair prior to the website launch. I'd like a 1 page flyer that highlights a sampling of some iconic pieces and invites people to check out the website soon. If possible, I'd also like a Word template for a tear sheet (a one page doc that has the company logo and contact info, a picture of the item, a field for description and dimensions). The following is an example of a tear sheet...http://www.kbtcabinetworks.example/uploads/4/8/1/3/4813902/vesper_oak_low_side_chair.pdf. I'd prefer a smaller slot for the image (maybe one side of the page) and a much larger area for description and dimensions (as its vintage furniture I'll need to report on condition).

I've attached a few sample pieces of furniture, the company logo, contact information, and a room that included furniture from the business. The color palette for the business is orange, black, white and gray.

Target Market(s)

Potential Customers.....

Industry/Entity Type

Retail

Font styles to use
Other font styles liked:
• I think the fonts should be similar to the ones used in the logo and the business card (see attached)

Colors
f37122
1b1b1b
ebebeb

Requirements
Must have
• An elegant clean look and feel (although its a mid century furniture business I don't carry kitschy items...just really beautiful classic high-end pieces). It should highlight the beauty of the furniture and provide contact information.

```html
<!DOCTYPE html>
<html lang="en">
<head>
<meta charset="utf-8">
<title>Atelier Greta Voss – Halvorsen Buffet</title>
<link href="https://fonts.googleapis.com/css2?family=Open+Sans:wght@300;400;700&display=swap" rel="stylesheet">
<style>
  :root {
    --orange: #f37122;
    --black: #1b1b1b;
    --gray: #ebebeb;
    --white: #ffffff;
    --wood: #2a1d17;
  }
  * { margin: 0; padding: 0; box-sizing: border-box; }
  html, body {
    width: 1200px; height: 1000px; overflow: hidden;
    background: var(--gray);
    font-family: "Open Sans", Arial, sans-serif;
  }
  .flyer {
    position: absolute; left: 340px; top: 0;
    width: 520px; height: 1000px;
    background: var(--white);
    overflow: hidden;
  }
  .brand {
    position: absolute; top: 218px; left: 0; width: 100%;
    text-align: center;
    font-weight: 300; font-size: 40px; letter-spacing: 1px;
    color: var(--black);
    text-transform: uppercase;
  }
  .stage { position: absolute; left: 0; top: 0; width: 520px; height: 1000px; }
  .product-photo {
    position: absolute; left: 43px; top: 343px;
    width: 435px; height: 267px;
    background: linear-gradient(180deg, #3a2a22 0%, var(--wood) 60%, #1a120e 100%);
  }
  .title {
    position: absolute; top: 654px; left: 0; width: 100%;
    text-align: center; color: var(--white);
  }
  .title-name { font-weight: 700; font-size: 38px; letter-spacing: 0.5px; line-height: 52px; }
  .title-type {
    display: flex; align-items: center; justify-content: center; gap: 4px;
    font-weight: 400; font-size: 34px; letter-spacing: 1px; line-height: 50px;
  }
  .title-type .rule { width: 52px; height: 2px; background: var(--white); }
  .contact {
    position: absolute; left: 0; bottom: 0; width: 100%; height: 72px;
    background: var(--black); color: var(--white);
    text-align: center; font-size: 10.5px; line-height: 14px;
    padding-top: 12px; text-transform: uppercase;
  }
  .contact-name { color: var(--orange); font-weight: 700; }
</style>
</head>
<body>
  <main class="flyer">
    <div class="brand">Atelier Greta Voss</div>

    <svg class="stage" viewBox="0 0 520 1000" aria-hidden="true">
      <polygon points="60,572 460,572 520,596 520,1000 0,1000 0,596" fill="var(--orange)"/>
      <ellipse cx="260" cy="604" rx="200" ry="10" fill="#000" opacity="0.18"/>
    </svg>

    <div class="product-photo" role="img" aria-label="Photo of a dark wood mid-century buffet with four drawers, two doors and brass pulls"></div>

    <div class="title">
      <div class="title-name">HALVORSEN</div>
      <div class="title-type"><span class="rule"></span>BUFFET<span class="rule"></span></div>
    </div>

    <footer class="contact">
      <div class="contact-name">Irena Kostelic</div>
      <div>Office 555-014-2090 &nbsp;|&nbsp; Mobile 555-016-5176</div>
      <div>irena@ateliergretavoss.example &nbsp;|&nbsp; www.ateliergretavoss.example</div>
    </footer>
  </main>
</body>
</html>
```